TrevanHollis's Signature Beard Oil Label Design

I'm looking for a creative designer to run with the design. I am not sure what I really want so surprise me. What ever you do please use earth tone colors. The bottles I use is 2.0 ounces. It is a Boston amber bottle with glass dropper. It is 1.5 width by 3.75 inch height. :Benefits : * Organic * Hair growth* Repairs Split Ends* Softens * Health Shine* Aromatherapy fragrance* Reduce Itching/Irritation * Reduce Dandruff* Reduces Flyaway hair Directions: Place a nickel size drop into palm of handMassage into beard 2 to 3 times a day

Target Market(s)

MEN WITH BEARDS AND MEN THAT WANT TO GROW BEARDS BUT DON'T KNOW HOW

Industry/Entity Type

Hair Care Product

Font styles to use
Serif
Script

Colors
1b1b1b
fdf9cf
ffc214
ffffff

Requirements
Must have
• FALL COLOR SCHEME, Trevan Hollis written in a fancy cursive script, all others can me different, please use the gold lion logo without the word Lion.
Nice to have
• CLASSY, MANLY, OLD AND NEW SCHOOL ESSENCE
Should not have
• Anything feminine, Flint Cove

```html
<!DOCTYPE html>
<html lang="en">
<head>
<meta charset="utf-8">
<title>Trevan Hollis Beard Oil Label</title>
<link rel="stylesheet" href="https://fonts.googleapis.com/css2?family=Kaushan+Script&family=Yellowtail&family=IM+Fell+English+SC&family=IM+Fell+English&display=block">
<style>
  :root {
    --page: #ffffff;
    --kraft: #cfc3a0;
    --panel: #8d6b12;
    --rule: #c9a326;
    --cream: #f6ebbd;
    --script-gold: #e2b548;
    --script-shadow: #3b2c05;
    --band: #5a4608;
    --band-text: #b8902a;
  }
  html, body {
    margin: 0;
    padding: 0;
    width: 1200px;
    height: 1199px;
    overflow: hidden;
    background: var(--page);
  }
  .canvas {
    position: relative;
    width: 1200px;
    height: 1199px;
  }
  .label-art {
    position: absolute;
    left: 0;
    top: 0;
  }
  .script {
    position: absolute;
    margin: 0;
    font-family: "Kaushan Script", "Yellowtail", cursive;
    font-weight: 400;
    font-style: normal;
    color: var(--script-gold);
    text-shadow: 2px 2px 0 var(--script-shadow);
    white-space: nowrap;
    line-height: 1;
  }
  .panel-title {
    font-size: 50px;
    transform: translate(-50%, -50%) rotate(-4deg);
  }
  .directions-title { left: 240px; top: 192px; }
  .benefits-title { left: 956px; top: 180px; }

  .directions-text {
    position: absolute;
    left: 42px;
    width: 415px;
    top: 245px;
    margin: 0;
    font-family: "IM Fell English SC", serif;
    font-size: 29px;
    line-height: 44px;
    color: var(--cream);
    text-align: center;
  }

  .benefit-list {
    position: absolute;
    top: 0;
    left: 0;
    margin: 0;
    padding: 0;
    list-style: none;
    font-family: "IM Fell English SC", serif;
    font-size: 19px;
    line-height: 22px;
    color: var(--cream);
    text-align: center;
  }
  .benefit-list li {
    position: absolute;
    width: 200px;
    transform: translate(-50%, -50%);
  }
  .benefit-list.left li { left: 860px; }
  .benefit-list.right li { left: 1054px; }

  .brand-name {
    font-size: 60px;
    text-shadow: 2px 3px 0 #2e2204;
    transform: translate(-50%, -50%) rotate(-15deg);
  }
  .brand-first { left: 594px; top: 200px; }
  .brand-last { left: 628px; top: 272px; }

  .product-band {
    position: absolute;
    left: 457px;
    top: 330px;
    width: 280px;
    height: 46px;
    background: var(--band);
    display: flex;
    align-items: center;
    justify-content: center;
    gap: 8px;
    font-family: "IM Fell English", serif;
    font-size: 34px;
    color: var(--band-text);
    letter-spacing: 1px;
  }
  .product-band::before,
  .product-band::after {
    content: "";
    position: absolute;
    left: 8px;
    right: 8px;
    height: 1px;
    background: var(--band-text);
  }
  .product-band::before { top: 5px; }
  .product-band::after { bottom: 5px; }
  .band-dots { font-size: 18px; }

  .brand-mark {
    position: absolute;
    left: 603px;
    top: 444px;
    transform: translate(-50%, -50%);
    display: flex;
    align-items: center;
    gap: 6px;
    font-family: "IM Fell English", serif;
    font-size: 18px;
    color: var(--panel);
    white-space: nowrap;
  }
  .brand-mark .mark-dot {
    width: 10px;
    height: 10px;
    border-radius: 50%;
    background: var(--panel);
  }

  .size-tag {
    position: absolute;
    left: 552px;
    top: 501px;
    width: 102px;
    height: 22px;
    background: var(--band);
    clip-path: polygon(8% 0, 92% 0, 100% 50%, 92% 100%, 8% 100%, 0 50%);
    font-family: "IM Fell English", serif;
    font-size: 20px;
    line-height: 22px;
    color: var(--band-text);
    text-align: center;
  }
</style>
</head>
<body>
<main class="canvas">
  <svg class="label-art" width="1200" height="1199" viewBox="0 0 1200 1199" aria-hidden="true">
    <defs>
      <linearGradient id="kraftShade" x1="0" y1="0" x2="1" y2="1">
        <stop offset="0" stop-color="#d3c7a5"/>
        <stop offset="1" stop-color="#c6b993"/>
      </linearGradient>
    </defs>
    <rect x="31" y="127" width="1147" height="373" fill="url(#kraftShade)"/>
    <rect x="42" y="139" width="415" height="350" fill="var(--panel)"/>
    <rect x="45" y="142" width="409" height="344" fill="none" stroke="var(--rule)" stroke-width="1.5"/>
    <rect x="750" y="139" width="418" height="350" fill="var(--panel)"/>
    <rect x="753" y="142" width="412" height="344" fill="none" stroke="var(--rule)" stroke-width="1.5"/>
    <path d="M464 150 Q464 86 603 86 Q742 86 742 150 L742 468 Q676 540 603 570 Q530 540 464 468 Z"
          fill="url(#kraftShade)"/>
    <path d="M474 155 Q474 98 603 98 Q732 98 732 155 L732 462 Q670 526 603 556 Q536 526 474 462 Z"
          fill="none" stroke="var(--rule)" stroke-width="2"/>
  </svg>

  <h2 class="script panel-title directions-title">Directions</h2>
  <p class="directions-text">
    Place a nickel size<br>
    drop into palm of hand<br>
    Massage into beard 2<br>
    to 3 times a day
  </p>

  <h2 class="script panel-title benefits-title">Benefits</h2>
  <ul class="benefit-list left">
    <li style="top:248px">Organic</li>
    <li style="top:294px">Hair growth</li>
    <li style="top:338px">Repairs Split Ends</li>
    <li style="top:383px">Softens</li>
    <li style="top:428px">Health Shine</li>
  </ul>
  <ul class="benefit-list right">
    <li style="top:252px">Aromatherapy</li>
    <li style="top:308px">Reduce<br>Itching/Irritation</li>
    <li style="top:364px">Reduce Dandruff</li>
    <li style="top:421px">Reduces Flyaway<br>hair</li>
  </ul>

  <h1 class="script brand-name brand-first">Trevan</h1>
  <span class="script brand-name brand-last">Hollis</span>

  <div class="product-band"><span class="band-dots">••</span>BEARD OIL<span class="band-dots">••</span></div>

  <div class="brand-mark"><span class="mark-dot"></span>Trevan Hollis</div>

  <div class="size-tag">2oz</div>
</main>
</body>
</html>
```